Kestrel Summit 2019 Enemies of the End-Times Church Flyer

We want a church conference flyer designed. We are looking for a professional, yet catchy design that uses our brand colors and logo creatively while communicating key information of the event effectively. <br/>The flyer must include all of the following:<br/>Title: Kestrel Summit 2019<br/>Topic: The Enemies of The End-Times Church <br/>Subtitles: <br/> -How the antichrist raises an army by social behavior engineering. <br/>-How the architects of modern social constructs escaped the church's radar. <br/>-The Holy Spirit's end-times agenda:<br/> The Knock-Out Punch!<br/>Speaker: Prophet Marcus Toliver <br/>Dates/time: December 27, 28 & 29 at 6pm<br/>Location: Halvorn Community Center <br/> 241 Pellham Street <br/> Portland, ME 04102<br/>Contact info: phone: 207-555-0148 <br/>email: contact@brookmeadow.example <br/> www.vutel.example<br/>*The flyer must also include a picture of the speaker and our Vutel logo <br/>Thanks, we look forward to seeing what you come up with!

Colors

Designer to choose colors to be used in the design.

Requirements
Must have
• The flyer must include all of the following:
• Title: Kestrel Summit 2019
• Topic: The Enemies of The End-Times Church
• Subtitles:
• -How the antichrist raises an army by social behavior engineering.
• -How the architects of modern social constructs escaped the church's radar.
• -The Holy Spirit's end-times agenda:
• The Knock-Out Punch!
• Speaker: Prophet Marcus Toliver
• Dates/time: December 27, 28 & 29 at 6pm
• Location: Halvorn Community Center
• 241 Pellham Street
• Portland, ME 04102
• Contact info: phone: 207-555-0148
• email: contact@brookmeadow.example
• www.vutel.example
• *The flyer must also include a picture of the speaker and our Vutel logo
Should not have
• Pictures of crosses or church buildings

```html
<!DOCTYPE html>
<html lang="en">
<head>
<meta charset="utf-8">
<title>Kestrel Summit 2019 Flyer</title>
<link rel="stylesheet" href="https://fonts.googleapis.com/css2?family=Montserrat:wght@700&family=Open+Sans:wght@400;700&family=Saira+Condensed:wght@300&family=Kaushan+Script&display=swap">
<style>
  :root {
    --page: #ffffff;
    --space-deep: #1a1238;
    --space-violet: #5b2f9a;
    --space-magenta: #c03bb8;
    --space-pink: #f08ad8;
    --white: #ffffff;
    --topic-cream: #fbe9c8;
    --topic-glow: #e07a2a;
    --ribbon-red: #e0141c;
    --ribbon-dark: #9c0a10;
    --navy: #123a5e;
    --navy-deep: #0b1526;
    --photo-tone: #6b5f5a;
  }
  * { margin: 0; padding: 0; box-sizing: border-box; }
  html, body { width: 1200px; height: 1000px; overflow: hidden; background: var(--page); }
  .canvas { position: relative; width: 1200px; height: 1000px; }
  .flyer { position: absolute; left: 243px; top: 38px; width: 712px; height: 922px; overflow: hidden; background: var(--page); }
  .space-backdrop {
    position: absolute; left: 0; top: 0; width: 712px; height: 700px;
    background:
      radial-gradient(ellipse 260px 220px at 300px 320px, rgba(220,140,200,.55), transparent 70%),
      radial-gradient(ellipse 500px 200px at 250px 560px, rgba(240,110,220,.75), transparent 75%),
      linear-gradient(180deg, var(--space-deep) 0%, var(--space-violet) 40%, var(--space-magenta) 72%, var(--space-pink) 86%, var(--page) 100%);
  }
  .title {
    position: absolute; left: 0; width: 712px; top: 52px; text-align: center;
    font-family: "Montserrat", sans-serif; font-weight: 700; font-size: 58px; line-height: 83px;
    color: var(--white); letter-spacing: 1px;
  }
  .topic {
    position: absolute; left: 0; width: 712px; top: 336px; text-align: center;
    font-family: "Saira Condensed", sans-serif; font-weight: 300; font-size: 42px; letter-spacing: 1.5px;
    color: var(--topic-cream); text-shadow: 0 0 6px var(--topic-glow), 0 0 12px var(--topic-glow);
  }
  .subtitles {
    position: absolute; left: 24px; top: 402px; list-style: none;
    font-family: "Open Sans", sans-serif; font-weight: 700; font-size: 15px; line-height: 23.5px;
    color: var(--white); text-shadow: 0 1px 2px rgba(0,0,0,.5);
  }
  .punchline {
    position: absolute; left: 0; width: 712px; top: 484px; text-align: center;
    font-family: "Kaushan Script", cursive; font-size: 36px; color: var(--white);
    text-shadow: 0 0 4px #000, 0 0 8px #000;
  }
  .ribbons { position: absolute; left: 110px; top: 550px; }
  .ribbon-text {
    position: absolute; text-align: center; font-family: "Open Sans", sans-serif;
    font-size: 24px; line-height: 31px; color: var(--white);
  }
  .ribbon-dates { left: 120px; top: 577px; width: 160px; }
  .ribbon-time { left: 324px; top: 594px; width: 170px; }
  .info-band {
    position: absolute; left: 10px; top: 757px; width: 540px; height: 154px;
    background: linear-gradient(90deg, var(--navy) 0%, var(--navy) 55%, var(--navy-deep) 100%);
  }
  .brand { position: absolute; left: 16px; top: 62px; display: flex; align-items: center; gap: 6px; }
  .brand-mark { width: 12px; height: 12px; border-radius: 50%; background: var(--white); }
  .brand-name { font-family: "Open Sans", sans-serif; font-weight: 400; font-size: 30px; color: var(--white); }
  .contact {
    position: absolute; left: 159px; top: 2px; width: 326px;
    font-family: "Open Sans", sans-serif; font-size: 16.5px; line-height: 25px; color: var(--white);
    font-style: normal; white-space: nowrap;
  }
  .speaker-photo {
    position: absolute; left: 497px; top: 557px; width: 215px; height: 365px;
    background: linear-gradient(180deg, rgba(255,255,255,0) 0%, var(--photo-tone) 30%, #3a3a40 65%, #2b2b30 100%);
  }
  .speaker-label {
    position: absolute; left: 497px; top: 862px; width: 208px; height: 52px;
    background: var(--navy); border: 2px solid var(--white); border-radius: 6px;
    text-align: center; font-family: "Open Sans", sans-serif; font-weight: 700; font-size: 15px; line-height: 20px;
    color: var(--white); padding-top: 4px;
  }
</style>
</head>
<body>
<div class="canvas">
  <div class="flyer">
    <div class="space-backdrop" role="img" aria-label="Starry purple and pink galaxy sky with a faint planet"></div>

    <h1 class="title">Kestrel Summit<br>2019</h1>
    <h2 class="topic">The Enemies of The End-Times Church</h2>
    <ul class="subtitles">
      <li>How the antichrist raises an army by social behavior engineering.</li>
      <li>How the architects of modern social constructs escaped the church's radar.</li>
      <li>The Holy Spirit's end-times agenda</li>
    </ul>
    <p class="punchline">The Knock-Out Punch!</p>

    <svg class="ribbons" width="400" height="220" viewBox="0 0 400 220" aria-hidden="true">
      <polygon points="40,100 100,100 80,170" fill="var(--ribbon-dark)"/>
      <polygon points="60,100 130,100 75,175" fill="var(--ribbon-red)"/>
      <polygon points="5,10 175,6 170,100 10,104" fill="var(--ribbon-red)"/>
      <polygon points="260,102 320,102 250,172" fill="var(--ribbon-dark)"/>
      <polygon points="230,102 300,102 245,175" fill="var(--ribbon-red)"/>
      <polygon points="212,6 385,10 380,104 217,100" fill="var(--ribbon-red)"/>
    </svg>
    <p class="ribbon-text ribbon-dates">December<br>27, 28 &amp; 29</p>
    <p class="ribbon-text ribbon-time">@ 6.00 PM</p>

    <div class="info-band">
      <div class="brand">
        <span class="brand-mark"></span>
        <span class="brand-name">Vutel</span>
      </div>
      <address class="contact">
        Location: Halvorn Community Center<br>
        241 Pellham Street<br>
        Portland, ME 04102<br>
        Contact info: phone: 207-555-0148<br>
        email: contact@brookmeadow.example<br>
        www.vutel.example
      </address>
    </div>

    <div class="speaker-photo" role="img" aria-label="Portrait photo of speaker Prophet Marcus Toliver in a dark blazer and red shirt"></div>
    <div class="speaker-label">Speaker:<br>Prophet Marcus Toliver</div>
  </div>
</div>
</body>
</html>
```